Law Office Business Card

We need a business card design to include the following information:
Name of Firm: Lindell Law Group, P.A.
Address: 4627 Harbin Rd, Ste 215, Maple Springs, GA 30512
Phone: 706-390-5817
Fax: 706-394-7752
Website: http://www.tlindellaw.com

We Need a place for the Person's name and email address. Please start with the following:
Denise K. Halbrook, Esq.
denise@tlindellaw.com

```html
<!DOCTYPE html>
<html lang="en">
<head>
<meta charset="utf-8">
<title>Lindell Law Group – Business Card</title>
<link rel="stylesheet" href="https://fonts.googleapis.com/css2?family=Marcellus&family=Open+Sans:wght@400;700&display=swap">
<style>
  :root {
    --page-bg: #eceef0;
    --card-white: #ffffff;
    --band-top: #e3eef9;
    --band-bottom: #b3cfeb;
    --firm-grey: #7d7670;
    --name-blue: #1d5478;
    --text-blue: #2a5a80;
    --rule-blue: #3c6a8c;
  }
  * { box-sizing: border-box; margin: 0; padding: 0; }
  html, body { width: 1200px; height: 993px; overflow: hidden; }
  body {
    background: var(--page-bg);
    font-family: "Open Sans", Arial, sans-serif;
  }
  .card {
    position: absolute;
    left: 100px;
    top: 210px;
    width: 1000px;
    height: 572px;
    background: var(--card-white);
    box-shadow: 0 10px 30px rgba(0,0,0,0.15);
    overflow: hidden;
  }
  .band {
    position: absolute;
    left: 0; right: 0; top: 250px; bottom: 0;
    background: linear-gradient(180deg, var(--band-top), var(--band-bottom));
  }
  .logo {
    position: absolute;
    left: 48px;
    top: 62px;
    width: 250px;
    display: flex;
    flex-direction: column;
    align-items: center;
    gap: 12px;
  }
  .logo-square {
    width: 74px; height: 74px;
    border: 2px solid var(--firm-grey);
  }
  .logo-name {
    font-family: "Marcellus", Georgia, serif;
    font-size: 30px;
    color: var(--firm-grey);
    white-space: nowrap;
  }
  .firm-name {
    position: absolute;
    right: 70px;
    top: 172px;
    font-family: "Marcellus", Georgia, serif;
    font-size: 50px;
    color: var(--firm-grey);
    letter-spacing: 1px;
    white-space: nowrap;
  }
  .person {
    position: absolute;
    left: 56px;
    top: 318px;
    font-size: 29px;
    font-weight: 700;
    letter-spacing: 1.5px;
    color: var(--name-blue);
    white-space: nowrap;
  }
  .divider {
    position: absolute;
    left: 478px;
    top: 268px;
    width: 4px;
    height: 210px;
    background: var(--rule-blue);
  }
  .contacts {
    position: absolute;
    left: 512px;
    top: 280px;
    list-style: none;
    color: var(--text-blue);
    font-size: 22px;
    line-height: 31px;
  }
  .contacts li { display: flex; align-items: flex-start; gap: 12px; }
  .contacts svg { flex: none; width: 20px; height: 20px; margin-top: 6px; fill: var(--text-blue); }
  .contacts .address { margin-bottom: 8px; }
</style>
</head>
<body>
  <div class="card">
    <div class="band"></div>

    <div class="logo">
      <div class="logo-square"></div>
      <div class="logo-name">Lindell Law Group</div>
    </div>

    <div class="firm-name">Lindell Law Group, P.A.</div>

    <div class="person">Denise K. Halbrook, Esq.</div>
    <div class="divider"></div>

    <ul class="contacts">
      <li class="address">
        <svg viewBox="0 0 20 20"><path d="M10 1a6 6 0 0 0-6 6c0 4.5 6 12 6 12s6-7.5 6-12a6 6 0 0 0-6-6zm0 8.5A2.5 2.5 0 1 1 10 4.5a2.5 2.5 0 0 1 0 5z"/></svg>
        <span>4627 Harbin Rd, Ste 215,<br>Maple Springs, GA 30512</span>
      </li>
      <li>
        <svg viewBox="0 0 20 20"><path d="M1 4h18v12H1z"/><path d="M1 4l9 7 9-7" fill="none" stroke="#fff" stroke-width="1.5"/></svg>
        <span>denise@tlindellaw.com</span>
      </li>
      <li>
        <svg viewBox="0 0 20 20"><rect x="1" y="1" width="18" height="18" rx="4"/><path d="M6 5l2 0 1 3-1.5 1a7 7 0 0 0 3.5 3.5l1-1.5 3 1 0 2c-5 0-9-4-9-9z" fill="#fff"/></svg>
        <span>706-390-5817</span>
      </li>
      <li>
        <svg viewBox="0 0 20 20"><rect x="5" y="1" width="10" height="6"/><rect x="1" y="7" width="18" height="12" rx="2"/><rect x="5" y="12" width="10" height="4" fill="#fff"/></svg>
        <span>706-394-7752</span>
      </li>
      <li>
        <svg viewBox="0 0 20 20"><circle cx="10" cy="10" r="9"/><path d="M1 10h18M10 1c-4 4-4 14 0 18M10 1c4 4 4 14 0 18" fill="none" stroke="#fff" stroke-width="1.2"/></svg>
        <span>www.tlindellaw.com</span>
      </li>
    </ul>
  </div>
</body>
</html>
```